Vell Studio - Lash Serum Packaging

Need Packaging done for this Lash Serum for a brand called "Vell Studio". The bottle will remain black but the box can be any color. This will be for a 3ml bottle. Give me different options for packaging that is minimalist and clean for this brand that makes it look expensive and make people want to buy.

```html
<!DOCTYPE html>
<html lang="en">
<head>
<meta charset="utf-8">
<title>Vell Studio – Lash Serum Box Dieline</title>
<link rel="stylesheet" href="https://fonts.googleapis.com/css2?family=Montserrat:wght@500;700;800&display=swap">
<style>
  :root {
    --backdrop: #ebe9df;
    --box-black: #050607;
    --cut-line: #1c9fd6;
    --gold: #d6ae4e;
    --gold-light: #f6e6a4;
    --gold-deep: #a9802c;
    --ink-dark: #16110a;
    --white: #ffffff;
  }
  html, body {
    margin: 0;
    width: 1200px;
    height: 1200px;
    overflow: hidden;
    background: var(--backdrop);
  }
  .dieline {
    display: block;
    width: 1200px;
    height: 1200px;
    font-family: "Montserrat", sans-serif;
  }
  .box-body { fill: var(--box-black); }
  .cut { fill: none; stroke: var(--cut-line); stroke-width: 1.2; }
  .brand-vertical { fill: var(--gold); font-weight: 800; font-size: 40px; letter-spacing: 2px; }
  .brand-small { fill: var(--gold); font-weight: 700; font-size: 21px; }
  .flap-title { fill: var(--white); font-weight: 700; font-size: 27px; }
  .band-frame { fill: none; stroke: var(--ink-dark); stroke-width: 2.5; }
  .band-text { fill: var(--ink-dark); font-weight: 800; font-size: 45px; }
  .volume { fill: var(--white); font-weight: 500; font-size: 26px; }
  .benefit-title { fill: var(--white); font-weight: 700; font-size: 11.5px; }
  .benefit-copy { fill: var(--white); font-weight: 500; font-size: 11.5px; }
  .icon-ring { fill: none; stroke: var(--white); stroke-width: 1.6; }
  .maker-note { fill: var(--white); font-weight: 500; font-size: 11.5px; }
  .maker-name { fill: var(--white); font-weight: 800; font-size: 18px; }
</style>
</head>
<body>
<svg class="dieline" viewBox="980 20 940 1560" xmlns="http://www.w3.org/2000/svg" aria-label="Vell Studio lash serum box, flat dieline">
  <defs>
    <linearGradient id="gold-band" x1="0" y1="0" x2="1" y2="1">
      <stop offset="0" stop-color="var(--gold-deep)"/>
      <stop offset="0.35" stop-color="var(--gold-light)"/>
      <stop offset="0.65" stop-color="var(--gold)"/>
      <stop offset="1" stop-color="var(--gold-light)"/>
    </linearGradient>
  </defs>

  <!-- box body -->
  <path class="box-body" d="M1030,198 H1270 V500 H1448 V30 H1688 V500 H1897 V1263 H1688 V1565 H1448 V1263 H1030 Z"/>

  <!-- cut and fold lines -->
  <g class="cut-lines">
    <polyline class="cut" points="1045,517 993,542 993,1222 1045,1247"/>
    <rect class="cut" x="1045" y="517" width="836" height="730"/>
    <line class="cut" x1="1255" y1="517" x2="1255" y2="1247"/>
    <line class="cut" x1="1463" y1="517" x2="1463" y2="1247"/>
    <line class="cut" x1="1672" y1="517" x2="1672" y2="1247"/>
    <path class="cut" d="M1045,517 V245 Q1045,213 1077,213 H1223 Q1255,213 1255,245 V517"/>
    <line class="cut" x1="1045" y1="307" x2="1255" y2="307"/>
    <path class="cut" d="M1463,517 V46 H1672 V517"/>
    <line class="cut" x1="1463" y1="98" x2="1672" y2="98"/>
    <line class="cut" x1="1463" y1="307" x2="1672" y2="307"/>
    <path class="cut" d="M1528,205 H1608 A16,16 0 0 1 1608,237 H1586 A18,18 0 0 1 1550,237 H1528 A16,16 0 0 1 1528,205 Z"/>
    <path class="cut" d="M1528,409 H1608 A16,16 0 0 0 1608,377 H1586 A18,18 0 0 0 1550,377 H1528 A16,16 0 0 0 1528,409 Z"/>
    <path class="cut" d="M1463,1247 V1518 Q1463,1550 1495,1550 H1640 Q1672,1550 1672,1518 V1247"/>
    <line class="cut" x1="1463" y1="1456" x2="1672" y2="1456"/>
  </g>

  <!-- top tuck flap -->
  <g class="top-flap">
    <text class="brand-small" x="1155" y="384" text-anchor="middle">VELL STUDIO</text>
    <text class="flap-title" x="1147" y="428" text-anchor="middle">LASH</text>
    <text class="flap-title" x="1147" y="452" text-anchor="middle">SERUM</text>
  </g>

  <!-- front panels -->
  <g class="front-panel">
    <text class="brand-vertical" transform="translate(1140,568) rotate(90)" textLength="272" lengthAdjust="spacing">VELL STUDIO</text>
    <rect x="1045" y="997" width="210" height="103" fill="url(#gold-band)"/>
    <rect class="band-frame" x="1055" y="1008" width="190" height="81"/>
    <text class="band-text" x="1150" y="1045" text-anchor="middle">LASH</text>
    <text class="band-text" x="1150" y="1084" text-anchor="middle">SERUM</text>
    <text class="volume" x="1193" y="1208" text-anchor="middle">3ml</text>
  </g>
  <g class="front-panel">
    <text class="brand-vertical" transform="translate(1349,568) rotate(90)" textLength="272" lengthAdjust="spacing">VELL STUDIO</text>
    <rect x="1255" y="997" width="208" height="103" fill="url(#gold-band)"/>
    <rect class="band-frame" x="1264" y="1008" width="190" height="81"/>
    <text class="band-text" x="1359" y="1045" text-anchor="middle">LASH</text>
    <text class="band-text" x="1359" y="1084" text-anchor="middle">SERUM</text>
    <text class="volume" x="1383" y="1208" text-anchor="middle">3ml</text>
  </g>
  <g class="front-panel">
    <text class="brand-vertical" transform="translate(1766,568) rotate(90)" textLength="272" lengthAdjust="spacing">VELL STUDIO</text>
    <rect x="1672" y="997" width="208" height="103" fill="url(#gold-band)"/>
    <rect class="band-frame" x="1681" y="1008" width="190" height="81"/>
    <text class="band-text" x="1776" y="1045" text-anchor="middle">LASH</text>
    <text class="band-text" x="1776" y="1084" text-anchor="middle">SERUM</text>
    <text class="volume" x="1818" y="1208" text-anchor="middle">3ml</text>
  </g>

  <!-- benefits panel -->
  <g class="benefits" text-anchor="middle">
    <g class="benefit-icon"><circle class="icon-ring" cx="1568" cy="562" r="16"/><path class="icon-ring" d="M1558,562 Q1568,570 1578,562"/></g>
    <text class="benefit-title" x="1568" y="596">Strengthening lashes:</text>
    <text class="benefit-copy" x="1568" y="611">Eyelash serum can help</text>
    <text class="benefit-copy" x="1568" y="626">strengthen lashes and make</text>
    <text class="benefit-copy" x="1568" y="641">them less likely to break.</text>

    <g class="benefit-icon"><circle class="icon-ring" cx="1568" cy="677" r="16"/><path class="icon-ring" d="M1558,677 Q1568,685 1578,677"/></g>
    <text class="benefit-title" x="1568" y="714">Extending growth cycle:</text>
    <text class="benefit-copy" x="1568" y="729">Eyelash serum can increase</text>
    <text class="benefit-copy" x="1568" y="744">the growth stage of the hair</text>
    <text class="benefit-copy" x="1568" y="759">follicle, which can help</text>
    <text class="benefit-copy" x="1568" y="774">lashes grow longer.</text>

    <g class="benefit-icon"><circle class="icon-ring" cx="1568" cy="807" r="16"/><path class="icon-ring" d="M1558,807 Q1568,815 1578,807"/></g>
    <text class="benefit-title" x="1568" y="847">Repairing damaged lashes:</text>
    <text class="benefit-copy" x="1568" y="862">Eyelash serum can help repair</text>
    <text class="benefit-copy" x="1568" y="877">damaged lashes and brows.</text>

    <g class="benefit-icon"><circle class="icon-ring" cx="1568" cy="901" r="16"/><path class="icon-ring" d="M1558,901 Q1568,909 1578,901"/></g>
    <text class="benefit-title" x="1568" y="935">Preventing breakage:</text>
    <text class="benefit-copy" x="1568" y="950">Eyelash serum can help</text>
    <text class="benefit-copy" x="1568" y="965">prevent lashes from breaking</text>
    <text class="benefit-copy" x="1568" y="980">and falling out.</text>

    <g class="benefit-icon"><circle class="icon-ring" cx="1568" cy="1007" r="16"/><path class="icon-ring" d="M1558,1007 Q1568,1015 1578,1007"/></g>
    <text class="benefit-title" x="1568" y="1038">Moisturizing lashes:</text>
    <text class="benefit-copy" x="1568" y="1053">Eyelash serum can</text>
    <text class="benefit-copy" x="1568" y="1068">help moisturize lashes and</text>
    <text class="benefit-copy" x="1568" y="1083">keep them healthy.</text>

    <g class="benefit-icon"><circle class="icon-ring" cx="1568" cy="1107" r="16"/><path class="icon-ring" d="M1558,1107 Q1568,1115 1578,1107"/></g>
    <text class="benefit-title" x="1568" y="1141">Improving appearance:</text>
    <text class="benefit-copy" x="1568" y="1156">Eyelash serum can help</text>
    <text class="benefit-copy" x="1568" y="1171">improve the appearance</text>
    <text class="benefit-copy" x="1568" y="1186">of lashes, making them</text>
  </g>

  <!-- bottom flap -->
  <g class="bottom-flap" text-anchor="middle">
    <text class="maker-note" x="1568" y="1331">Manufactured &amp;</text>
    <text class="maker-note" x="1568" y="1346">Marketed BY:</text>
    <text class="maker-name" x="1568" y="1400">VELL STUDIO</text>
  </g>
</svg>
</body>
</html>
```